Marketing company needs business card design

Our company (Ventures Beyond Harbor) need a business card design for a marketing company. The design should of course include the logo and business colors (orange and blue). I would like the design to be clean and professional. The business card is going to be a die cut card that is leaf shaped (I have uploaded the template for it). I would love to see a design that is professional but nothing too "corporate."
Updates

Hello everyone,

Just wanted to let you know that I have uploaded an AI and EPS version of the logo for your convenience.

Thank you!

~Marlene

Industry/Entity Type

Marketing

Requirements
Must have
• Must have the following contact info:

Ventures Beyond Harbor
2817 Hollow Brook Ln B204
Prescott, AZ 86517

928.471.6083

info@venturesbeyondharbor-example.com

```html
<!DOCTYPE html>
<html lang="en">
<head>
<meta charset="utf-8">
<title>Ventures Beyond Harbor — Business Card</title>
<link rel="stylesheet" href="https://fonts.googleapis.com/css2?family=Didact+Gothic&display=swap">
<style>
  :root {
    --backdrop: #4a3f36;
    --card: #ffffff;
    --brand-blue: #2ea6dc;
    --brand-orange: #eda24a;
    --text-grey: #8c8c8c;
    --art-light: #d6ecf7;
    --art-deep: #8fcdee;
  }
  * { margin: 0; padding: 0; box-sizing: border-box; }
  html, body {
    width: 1200px;
    height: 520px;
    overflow: hidden;
    background: var(--backdrop);
    font-family: "Didact Gothic", "Century Gothic", sans-serif;
  }
  .canvas { position: relative; width: 1200px; height: 520px; }

  .card {
    position: absolute;
    top: 127px;
    width: 492px;
    height: 280px;
    background: var(--card);
    overflow: hidden;
  }
  .card--back  { left: 65px;  border-radius: 104px 0 104px 0; }
  .card--front { left: 645px; border-radius: 0 104px 0 104px; }

  .brand-mark {
    position: absolute;
    top: 24px;
    display: flex;
    align-items: center;
    gap: 7px;
    color: var(--brand-blue);
    font-size: 15px;
    line-height: 1.15;
  }
  .brand-mark__dot {
    width: 14px;
    height: 14px;
    border-radius: 50%;
    background: var(--brand-orange);
    flex: none;
  }
  .card--back .brand-mark  { right: 28px; }
  .card--front .brand-mark { left: 18px; }

  .cloud-art {
    position: absolute;
    left: 30px;
    top: 63px;
    width: 385px;
    height: 217px;
    background: linear-gradient(160deg, var(--art-light) 0%, var(--art-deep) 100%);
  }

  .contact {
    position: absolute;
    left: 143px;
    top: 104px;
    font-style: normal;
    color: var(--text-grey);
  }
  .contact__name {
    font-size: 19px;
    color: var(--brand-blue);
    margin-bottom: 6px;
  }
  .contact__name .accent { color: var(--brand-orange); }
  .contact__line { font-size: 17px; line-height: 27px; }
  .contact__email {
    margin-top: 22px;
    font-size: 14px;
    color: var(--brand-blue);
  }
</style>
</head>
<body>
<main class="canvas">
  <section class="card card--back">
    <div class="brand-mark">
      <span class="brand-mark__dot"></span>
      <span>Ventures<br>Beyond Harbor</span>
    </div>
    <div class="cloud-art" role="img" aria-label="Large light blue cloud illustration with a dotted blue pattern"></div>
  </section>

  <section class="card card--front">
    <div class="brand-mark">
      <span class="brand-mark__dot"></span>
      <span>Ventures<br>Beyond Harbor</span>
    </div>
    <address class="contact">
      <p class="contact__name">Ventures <span class="accent">Beyond</span> Harbor</p>
      <p class="contact__line">2817 Hollow Brook Ln B204</p>
      <p class="contact__line">Prescott, AZ 86517</p>
      <p class="contact__line">928.471.6083</p>
      <p class="contact__email">info@venturesbeyondharbor-example.com</p>
    </address>
  </section>
</main>
</body>
</html>
```